Marrow medical spa and wellness

Integrate existing logo and web design (colors and background) into tri fold, single card brochure and business card design. We already have a logo and an idea for our promotional material but we would like someone to bring it together for us! Quenvoraspaandwellness.com. We want to see what a marble background with a faded lily (as seen on our webpage) would look like on brochures and business cards.

```html
<!DOCTYPE html>
<html lang="en">
<head>
<meta charset="utf-8">
<title>Marrow Medical Spa &amp; Wellness — Business Card Options</title>
<link rel="stylesheet" href="https://fonts.googleapis.com/css2?family=Crimson+Text&family=Pinyon+Script&family=Montserrat:wght@500&display=swap">
<style>
  :root {
    --stage-light: #a9b1b5;
    --stage-dark: #5b6166;
    --card-dark: #262626;
    --card-dark-hi: #3d3d3d;
    --marble-light: #f7f7f7;
    --marble-mid: #e6e7e8;
    --gold: #c9a32a;
    --gold-deep: #b48a18;
    --ink: #2a2a2a;
    --rule: #8a8a8a;
    --label: #b9c0c4;
  }
  * { box-sizing: border-box; margin: 0; padding: 0; }
  html, body { width: 745px; height: 1200px; overflow: hidden; }
  body { font-family: "Crimson Text", Georgia, serif; color: var(--ink); }

  .option {
    position: relative;
    width: 745px;
    height: 600px;
    background: radial-gradient(ellipse at 35% 40%, var(--stage-light), var(--stage-dark) 95%);
  }
  .option + .option { border-top: 1px solid #6c7277; }

  .card {
    position: absolute;
    width: 340px;
    height: 194px;
    overflow: hidden;
    box-shadow: 0 10px 22px rgba(0,0,0,.35);
  }
  .card-back { left: 30px; top: 80px; background: linear-gradient(200deg, var(--card-dark-hi), var(--card-dark) 60%); }
  .card-front { left: 375px; top: 250px; }

  .lily-petals {
    position: absolute;
    left: 14px; top: 48px;
    width: 200px; height: 146px;
    border-radius: 60% 40% 0 0;
    background: linear-gradient(160deg, #f2f2f2, #d9dadb 70%, #c8c9ca);
  }
  .marble {
    position: absolute; inset: 0;
    background: linear-gradient(135deg, var(--marble-light), var(--marble-mid) 45%, var(--marble-light) 60%, #ececec);
  }

  .brand-name {
    position: absolute;
    font-family: "Crimson Text", Georgia, serif;
    color: var(--gold);
    display: flex; align-items: center; gap: 6px;
    white-space: nowrap;
  }
  .brand-dot { width: 10px; height: 10px; border-radius: 50%; background: var(--gold); }
  .card-back .brand-name { right: 38px; top: 52px; font-size: 26px; }

  .divider { position: absolute; left: 135px; top: 24px; width: 1px; height: 146px; background: var(--rule); }
  .divider::after {
    content: ""; position: absolute; left: -3px; top: 70px;
    width: 7px; height: 7px; border-radius: 50%; background: #555;
  }
  .front-brand { left: 0; width: 135px; top: 80px; justify-content: center; font-size: 24px; }
  .front-brand.wordmark { top: 72px; font-size: 15px; white-space: normal; text-align: center; line-height: 1.15; padding: 0 10px; }

  .contact { position: absolute; left: 150px; top: 20px; right: 10px; }
  .person-name { font-family: "Pinyon Script", cursive; color: var(--gold); font-size: 27px; line-height: 1; }
  .person-title { font-size: 9.5px; margin: 1px 0 10px 8px; }
  .contact-list { list-style: none; }
  .contact-list li { display: flex; align-items: center; gap: 6px; font-size: 9px; margin-bottom: 4px; }
  .contact-icon { width: 13px; height: 13px; flex: none; }
  .address { font-size: 9px; line-height: 1.2; margin: 10px 0 0 30px; }

  .option-label {
    position: absolute; right: 40px; bottom: 45px;
    font-family: "Montserrat", Arial, sans-serif; font-weight: 500;
    font-size: 36px; letter-spacing: 2px; color: var(--label);
  }
</style>
</head>
<body>

<section class="option">
  <div class="card card-back">
    <div class="lily-petals" role="img" aria-label="Faded white marble lily petals rising from the lower left"></div>
    <div class="brand-name"><span class="brand-dot"></span>Marrow</div>
  </div>
  <div class="card card-front">
    <div class="marble" role="img" aria-label="Soft white marble texture"></div>
    <div class="brand-name front-brand"><span class="brand-dot"></span>Marrow</div>
    <div class="divider"></div>
    <div class="contact">
      <p class="person-name">Lena Harrow</p>
      <p class="person-title">FNP-C, co-owner</p>
      <ul class="contact-list">
        <li><svg class="contact-icon" viewBox="0 0 14 14"><circle cx="7" cy="7" r="7" fill="var(--gold)"/><path d="M4.5 4 L6 4 L6.5 5.8 L5.7 6.4 Q6.5 8 7.8 8.5 L8.4 7.8 L10 8.4 L10 9.8 Q6 10 4.5 4Z" fill="#fff"/></svg>(555) 014-2290</li>
        <li><svg class="contact-icon" viewBox="0 0 14 14"><circle cx="7" cy="7" r="7" fill="var(--gold)"/><rect x="3.8" y="4.8" width="6.4" height="4.4" fill="none" stroke="#fff" stroke-width=".9"/><path d="M3.8 4.8 L7 7.4 L10.2 4.8" fill="none" stroke="#fff" stroke-width=".9"/></svg>welcome@quenvoraspaandwellness.com</li>
        <li><svg class="contact-icon" viewBox="0 0 14 14"><circle cx="7" cy="7" r="7" fill="var(--gold)"/><g fill="none" stroke="#fff" stroke-width=".8"><circle cx="7" cy="7" r="3.4"/><ellipse cx="7" cy="7" rx="1.4" ry="3.4"/><path d="M3.6 7 H10.4"/></g></svg>www.quenvoraspaandwellness.com</li>
      </ul>
      <p class="address">1420 N. Alder Lane, Suite 12<br>Fairview, AZ 85000</p>
    </div>
  </div>
  <p class="option-label">OPT_01</p>
</section>

<section class="option">
  <div class="card card-back">
    <div class="lily-petals" role="img" aria-label="Faded white marble lily petals rising from the lower left"></div>
    <div class="brand-name"><span class="brand-dot"></span>Marrow</div>
  </div>
  <div class="card card-front">
    <div class="marble" role="img" aria-label="Soft white marble texture"></div>
    <div class="brand-name front-brand wordmark">Marrow medical spa &amp; wellness</div>
    <div class="divider"></div>
    <div class="contact">
      <p class="person-name">Lena Harrow</p>
      <p class="person-title">FNP-C, co-owner</p>
      <ul class="contact-list">
        <li><svg class="contact-icon" viewBox="0 0 14 14"><circle cx="7" cy="7" r="7" fill="var(--gold)"/><path d="M4.5 4 L6 4 L6.5 5.8 L5.7 6.4 Q6.5 8 7.8 8.5 L8.4 7.8 L10 8.4 L10 9.8 Q6 10 4.5 4Z" fill="#fff"/></svg>(555) 014-2290</li>
        <li><svg class="contact-icon" viewBox="0 0 14 14"><circle cx="7" cy="7" r="7" fill="var(--gold)"/><rect x="3.8" y="4.8" width="6.4" height="4.4" fill="none" stroke="#fff" stroke-width=".9"/><path d="M3.8 4.8 L7 7.4 L10.2 4.8" fill="none" stroke="#fff" stroke-width=".9"/></svg>welcome@quenvoraspaandwellness.com</li>
        <li><svg class="contact-icon" viewBox="0 0 14 14"><circle cx="7" cy="7" r="7" fill="var(--gold)"/><g fill="none" stroke="#fff" stroke-width=".8"><circle cx="7" cy="7" r="3.4"/><ellipse cx="7" cy="7" rx="1.4" ry="3.4"/><path d="M3.6 7 H10.4"/></g></svg>www.quenvoraspaandwellness.com</li>
      </ul>
      <p class="address">1420 N. Alder Lane, Suite 12<br>Fairview, AZ 85000</p>
    </div>
  </div>
  <p class="option-label">OPT_02</p>
</section>

</body>
</html>
```